LANDCAPE Business Card Design

We need a business card design close to what we are sending you, just more professional. We are a landscape management company located on Topsail Island so an island theme would be great. We would like to stay with a black background and bright green lettering. Something to stand out.

Target Market(s)

Commercial and private property owners

Industry/Entity Type

Landscape

Contact Information for Business Card

BRACKENFORD GROUNDS CARE, LLC,DISCOVER YOUR PERSONAL PARADISE, WADE PELLIN 336-555-0184, MILES DORAHT 910-555-0137

Font styles to use
Sans Serif

```html
<!DOCTYPE html>
<html lang="en">
<head>
<meta charset="utf-8">
<title>Brackenford Grounds Care – Business Card</title>
<link href="https://fonts.googleapis.com/css2?family=Montserrat:ital,wght@0,700;0,800;1,700&display=swap" rel="stylesheet">
<style>
  :root {
    --page: #ffffff;
    --card: #000000;
    --green: #3bb54a;
    --green-soft: #36a844;
    --sea: #1d9fdc;
    --sea-light: #6cc7ef;
    --foam: #ffffff;
    --sand: #ffffff;
    --palm-glow: rgba(255, 255, 255, 0.85);
  }
  html, body {
    margin: 0;
    padding: 0;
    width: 1200px;
    height: 779px;
    overflow: hidden;
    background: var(--page);
  }
  .canvas {
    position: relative;
    width: 1200px;
    height: 779px;
  }
  .card {
    position: absolute;
    left: 115px;
    top: 112px;
    width: 979px;
    height: 553px;
    background: var(--card);
    overflow: hidden;
    font-family: "Montserrat", "Helvetica Neue", Arial, sans-serif;
  }
  .palms {
    position: absolute;
    left: 650px;
    top: 150px;
    width: 329px;
    height: 350px;
    background: radial-gradient(ellipse 55% 50% at 50% 52%, var(--palm-glow) 0%, rgba(255,255,255,0.45) 45%, rgba(255,255,255,0) 100%);
  }
  .card-shapes {
    position: absolute;
    inset: 0;
    width: 979px;
    height: 553px;
  }
  .brand-name {
    position: absolute;
    left: 46px;
    top: 40px;
    margin: 0;
    font-size: 82px;
    line-height: 1;
    font-weight: 800;
    color: var(--green);
    letter-spacing: 0.5px;
  }
  .brand-sub {
    position: absolute;
    left: 154px;
    top: 142px;
    margin: 0;
    font-size: 46px;
    line-height: 1;
    font-weight: 700;
    color: var(--green);
  }
  .contact {
    position: absolute;
    width: 300px;
    margin-left: -150px;
    text-align: center;
    color: var(--green-soft);
    font-weight: 700;
  }
  .contact-left { left: 172px; top: 290px; }
  .contact-right { left: 481px; top: 282px; }
  .contact-name {
    display: block;
    font-size: 24px;
    line-height: 1;
  }
  .contact-phone {
    display: block;
    margin-top: 10px;
    font-size: 27px;
    line-height: 1;
  }
  .tagline {
    position: absolute;
    left: 21px;
    top: 501px;
    margin: 0;
    font-size: 24px;
    line-height: 1;
    font-style: italic;
    font-weight: 700;
    color: var(--foam);
  }
</style>
</head>
<body>
<div class="canvas">
  <section class="card">
    <div class="palms" role="img" aria-label="White silhouette of a cluster of palm trees on the island"></div>

    <svg class="card-shapes" viewBox="0 0 979 553" aria-hidden="true">
      <path class="sea-light" d="M0,432 C130,395 260,410 400,455 C500,488 600,505 700,512 L700,553 L0,553 Z" fill="var(--sea-light)"/>
      <path class="sea" d="M0,448 C130,412 260,428 400,472 C500,502 590,515 670,520 L507,553 L0,553 Z" fill="var(--sea)"/>
      <path class="foam-line" d="M0,426 C130,388 260,403 400,448 C500,481 600,498 720,506" fill="none" stroke="var(--foam)" stroke-width="5"/>
      <path class="foam-line" d="M0,440 C130,404 260,419 400,464 C500,495 600,510 690,515" fill="none" stroke="var(--foam)" stroke-width="3"/>
      <path class="island" d="M470,553 C600,512 760,476 860,480 C920,483 960,490 979,495 L979,553 Z" fill="var(--sand)"/>
    </svg>

    <h1 class="brand-name">Brackenford</h1>
    <p class="brand-sub">Grounds Care, LLC</p>

    <div class="contact contact-left">
      <span class="contact-name">Wade Pellin</span>
      <span class="contact-phone">336-555-0184</span>
    </div>
    <div class="contact contact-right">
      <span class="contact-name">Miles Doraht</span>
      <span class="contact-phone">910-555-0137</span>
    </div>

    <p class="tagline">Discover your personal paradise</p>
  </section>
</div>
</body>
</html>
```